Gold Buyer Business Card

We are looking for a card that catches attention and that someone will remember. It should have a listing of items that we buy as well as a legal disclaimer which will be provided upon request. We have attached our company logo and a photo of a design that I liked for your reference but lets see what the crowd can come up with.
thanks and good luck!!

We Buy Gold & Silver;
Antique Jewelry
Bent/Broken Jewelry
Bracelets
Bullion
Coins
Chains
Dental Gold
Earrings
Rings
Scrap Gold
Silverware/Flatware
Used Jewelry

"Best Price Guaranteed"

Please use graphics of gold jewelry piles. I want some white in order for someone to write on.

Reason: I am looking for more designs with gold jewelry and coins on them. thanks

Industry/Entity Type

Legal

Requirements
Must have
• I would like this to have pictures of gold and silver. Maybe some jewelry in a pile. We are a company that buys scrap gold and jewelry. I would like to see some boldness, this card is a marketing tool and it should leave an impression.
Should not have
• These cards need to promote the company not an individual, no names on the card.

```html
<!DOCTYPE html>
<html lang="en">
<head>
<meta charset="utf-8">
<title>Harbor Metal Traders – Business Card</title>
<link rel="stylesheet" href="https://fonts.googleapis.com/css2?family=Exo+2:wght@400;600;700&display=swap">
<style>
  :root{
    --stage:#e4e4e2;
    --card-black:#050505;
    --gold:#caa03a;
    --gold-dark:#a87f25;
    --brand-gold:#e2b93b;
    --ink-light:#ffffff;
    --ink-soft:#d9d9d9;
    --write-white:#ffffff;
    --rule:#c9c9c9;
  }
  *{margin:0;padding:0;box-sizing:border-box}
  html,body{width:1200px;height:1047px;overflow:hidden;background:var(--stage)}
  body{position:relative;font-family:"Exo 2",sans-serif}
  .card{
    position:absolute;left:180px;width:840px;height:480px;
    background:var(--card-black);overflow:hidden;
    box-shadow:0 6px 18px rgba(0,0,0,.25);
  }
  .card--back{top:29px}
  .card--front{top:538px}

  .brand{
    display:flex;align-items:center;gap:14px;
    color:var(--brand-gold);font-weight:700;text-transform:uppercase;
    letter-spacing:1px;line-height:1.05;
  }
  .brand__dot{border-radius:50%;background:var(--brand-gold);flex:none}

  /* back */
  .card--back .brand{
    position:absolute;left:50%;top:96px;transform:translateX(-50%);
    font-size:52px;white-space:nowrap;
  }
  .card--back .brand__dot{width:40px;height:40px}
  .tagline{
    position:absolute;left:0;right:0;top:178px;text-align:center;
    color:var(--ink-light);font-size:22px;font-weight:600;
    letter-spacing:4px;text-transform:uppercase;
  }
  .write-space{
    position:absolute;left:120px;top:260px;width:600px;height:160px;
    background:var(--write-white);border-radius:4px;
    padding:36px 30px 0;
  }
  .write-space__line{height:1px;background:var(--rule);margin-bottom:40px}

  /* front */
  .bands{position:absolute;inset:0;width:840px;height:480px}
  .band{fill:var(--gold)}
  .band-fold{fill:var(--gold-dark)}

  .card--front .brand{position:absolute;left:36px;top:150px;font-size:30px}
  .card--front .brand__dot{width:26px;height:26px}

  .buy-list{position:absolute;left:360px;top:124px;width:450px;color:var(--ink-light)}
  .buy-list__title{
    font-size:18px;font-weight:700;letter-spacing:2px;text-transform:uppercase;
    color:var(--brand-gold);margin-bottom:8px;text-align:right;
  }
  .buy-list__items{
    list-style:none;display:grid;grid-template-columns:repeat(3,150px);
    font-size:13px;line-height:21px;color:var(--ink-soft);
  }
  .buy-list__items li::before{content:"• ";color:var(--brand-gold)}

  .jewelry-art{
    position:absolute;left:24px;top:356px;width:296px;height:108px;border-radius:4px;
    background:radial-gradient(circle at 35% 40%,#f3d77a 0%,#d4a634 40%,#8c6a1c 75%,#b9b9b9 100%);
  }

  .contacts{position:absolute;right:40px;top:304px;list-style:none;color:var(--ink-light);font-size:16px;letter-spacing:1px}
  .contacts li{display:flex;justify-content:flex-end;align-items:center;gap:12px;height:26px}
  .contacts svg{width:17px;height:17px;fill:none;stroke:var(--ink-light);stroke-width:2;stroke-linecap:round;stroke-linejoin:round}
  .address{position:absolute;right:40px;top:444px;color:var(--ink-soft);font-size:14px;letter-spacing:1px}
</style>
</head>
<body>

<section class="card card--back" aria-label="Card back">
  <div class="brand"><span class="brand__dot"></span><span>Harbor Metal Traders</span></div>
  <div class="tagline">“Best Price Guaranteed”</div>
  <div class="write-space" aria-label="Space for handwritten notes">
    <div class="write-space__line"></div>
    <div class="write-space__line"></div>
    <div class="write-space__line"></div>
  </div>
</section>

<section class="card card--front" aria-label="Card front">
  <svg class="bands" viewBox="0 0 840 480" aria-hidden="true">
    <polygon class="band" points="0,20 300,20 350,70 840,70 840,110 340,110 290,60 0,60"/>
    <polygon class="band-fold" points="300,20 350,70 340,110 290,60"/>
    <polygon class="band" points="0,300 290,300 340,250 840,250 840,290 350,290 300,340 0,340"/>
    <polygon class="band-fold" points="290,300 340,250 350,290 300,340"/>
  </svg>

  <div class="brand"><span class="brand__dot"></span><span>Harbor Metal<br>Traders</span></div>

  <div class="buy-list">
    <div class="buy-list__title">We Buy Gold &amp; Silver</div>
    <ul class="buy-list__items">
      <li>Antique Jewelry</li><li>Bent/Broken Jewelry</li><li>Bracelets</li>
      <li>Bullion</li><li>Coins</li><li>Chains</li>
      <li>Dental Gold</li><li>Earrings</li><li>Rings</li>
      <li>Scrap Gold</li><li>Silverware/Flatware</li><li>Used Jewelry</li>
    </ul>
  </div>

  <div class="jewelry-art" role="img" aria-label="Pile of gold and silver jewelry and coins"></div>

  <ul class="contacts">
    <li>014 555 0182
      <svg viewBox="0 0 24 24" aria-hidden="true"><path d="M5 3h4l2 5-3 2a11 11 0 0 0 6 6l2-3 5 2v4a2 2 0 0 1-2 2A17 17 0 0 1 3 5a2 2 0 0 1 2-2z"/></svg></li>
    <li>014 555 0183
      <svg viewBox="0 0 24 24" aria-hidden="true"><rect x="7" y="2" width="10" height="20" rx="2"/><path d="M11 18h2"/></svg></li>
    <li>014 555 0184
      <svg viewBox="0 0 24 24" aria-hidden="true"><rect x="3" y="9" width="18" height="11" rx="1"/><path d="M7 9V3h10v6M7 14h4M7 17h10"/></svg></li>
    <li>hello@harbormetal.net
      <svg viewBox="0 0 24 24" aria-hidden="true"><rect x="3" y="5" width="18" height="14" rx="1"/><path d="M3 6l9 7 9-7"/></svg></li>
    <li>www.harbormetal.net
      <svg viewBox="0 0 24 24" aria-hidden="true"><circle cx="12" cy="12" r="9"/><path d="M3 12h18M12 3c3 3 3 15 0 18M12 3c-3 3-3 15 0 18"/></svg></li>
  </ul>
  <div class="address">27 Quayside Row, 4th Floor, Marlow Bay</div>
</section>

</body>
</html>
```